Fernbrook Pet Showcase Ticket Card Design

We’re looking to create a complimentary “ticket” card for Fernbrook Pet Showcase that can be handed out physically. We host an event for cat lovers. The card should feel special and collectible. Size will be a standard business card (3.5" x 2") Orientation is open to designer recommendation. This ticket will be used as a complimentary entry pass for select guests, partners, & giveaways. Key elements to Include are the Fernbrook Pet Showcase logo (provided), the words “Complimentary Ticket” or similar wording (open to creative phrasing and cat puns) A blank space for the Event date (to be written in) & Ticket number (to be written in) . Event Name is always "Fernbrook Pet Bazaar & Rehoming Day". We want the ticket to feel clean & modern but slightly playful with a cat-inspired touch (think clever, not kitschy). Could include a subtle cat motif or texture (e.g., whisker lines, paw detail, soft patterning) Open to unique layout ideas that still leave clear writing space. Avoid overcrowding of elements. Ticket should also have fine print "This ticket is not redeemable for cash and cannot be combined with any other offers or discounts, can only be used for the date indicated"

Target Market(s)

Women

Industry/Entity Type

pets

Colors
6B429C
8869AF
B7A5CE
E3DAEB
F3F0F8

Requirements
Must have
• Fernbrook Pet Showcase Logo & words around complimentary ticket as well as the fine print
Nice to have
• cat-inspired touch (think clever, not kitschy). Could include a subtle cat motif or texture (e.g., whisker lines, paw detail, soft patterning)
Should not have
• should not look cartoony

```html
<!DOCTYPE html>
<html lang="en">
<head>
<meta charset="utf-8">
<title>Fernbrook Pet Showcase – Complimentary Ticket</title>
<link href="https://fonts.googleapis.com/css2?family=Montserrat:wght@400;500;600&display=swap" rel="stylesheet">
<style>
  :root {
    --backdrop: #979797;
    --card: #ffffff;
    --ink: #1c1c1c;
    --ink-soft: #2e2e2e;
    --rule: #1c1c1c;
  }
  * { margin: 0; padding: 0; box-sizing: border-box; }
  html, body {
    width: 1200px;
    height: 1108px;
    overflow: hidden;
    background: var(--backdrop);
    font-family: "Montserrat", Arial, sans-serif;
    color: var(--ink);
  }
  .canvas { position: relative; width: 1200px; height: 1108px; }
  .ticket {
    position: absolute;
    left: 242px;
    width: 716px;
    height: 409px;
    background: var(--card);
    border-radius: 26px;
    text-align: center;
  }
  .ticket--back { top: 119px; }
  .ticket--front { top: 581px; }

  .brand-name {
    position: absolute;
    left: 0; right: 0;
    font-weight: 600;
    color: var(--ink);
    letter-spacing: 0.01em;
    line-height: 1.08;
  }
  .ticket--back .brand-name { top: 62px; font-size: 54px; }
  .ticket--front .brand-name { top: 48px; font-size: 44px; }

  .fine-print {
    position: absolute;
    top: 292px; left: 0; right: 0;
    font-size: 18px;
    line-height: 29px;
    font-weight: 400;
    color: var(--ink);
    letter-spacing: 0.02em;
  }

  .ticket-title {
    position: absolute;
    top: 222px; left: 0; right: 0;
    font-size: 34px;
    font-weight: 400;
    color: var(--ink-soft);
    letter-spacing: 0.02em;
  }
  .event-name {
    position: absolute;
    top: 282px; left: 0; right: 0;
    font-size: 27px;
    font-weight: 400;
    color: var(--ink-soft);
    letter-spacing: 0.01em;
  }
  .write-in {
    position: absolute;
    top: 338px; left: 50px; right: 50px;
    display: flex;
    align-items: baseline;
    justify-content: center;
    font-size: 33px;
    font-weight: 400;
    color: var(--ink-soft);
  }
  .write-in__label { white-space: nowrap; }
  .write-in__blank {
    display: inline-block;
    width: 174px;
    height: 0;
    border-bottom: 2px solid var(--rule);
    margin: 0 10px 0 4px;
  }
  .write-in__blank:last-child { margin-right: 0; }
</style>
</head>
<body>
  <main class="canvas">
    <section class="ticket ticket--back" aria-label="Ticket reverse">
      <h2 class="brand-name">Fernbrook<br>Pet Showcase</h2>
      <p class="fine-print">
        This ticket is not redeemable for cash<br>
        Cannot be combined with other offers or discounts<br>
        Valid only for the date indicated
      </p>
    </section>

    <section class="ticket ticket--front" aria-label="Ticket front">
      <h1 class="brand-name">Fernbrook<br>Pet Showcase</h1>
      <p class="ticket-title">Complimentary Ticket</p>
      <p class="event-name">Fernbrook Pet Bazaar &amp; Rehoming Day</p>
      <p class="write-in">
        <span class="write-in__label">Date:</span><span class="write-in__blank"></span>
        <span class="write-in__label">Ticket No:</span><span class="write-in__blank"></span>
      </p>
    </section>
  </main>
</body>
</html>
```